Website for new slot-booking/reservations website/software

For a new software product we need a brand new logo and website for a reservations/booking system. The website should ideally present the main features with information text, contact info, news page as well as registration and pricing pages. As currently primary field of operation the software should be used for tennis but later on, also for other sport types. Also we'd like to be the logo a text-brand which includes the name "feldreserva.net" or just "feldreserva". The logo should ideally include an icon-design in some way. Generally we are open for ideas.

Bootstrap 4 template is a minimum requirement. (Multi-Page preferred, Single-Page still OK.)

You can use the attached image as an inspiration, but change of colors or other design elements are up to you. Currently the application has a primary color of #5500ff. The website created by you will not include the application itself, so it can have different (but ideally similar) Look&Feel.

Target Market(s)

Sports, Club-Management

Logo Text

feldreserva.net

Coding

Coded - Design and coding required

Number of Pages Required

5+ page

Font styles to use
Sans Serif

Requirements
Must have
• Bootstrap 4 Template, SCSS
Nice to have
• Rapid Loading Times, not too much external JS Libraries.
Should not have
• Extensive animations

```html
<!DOCTYPE html>
<html lang="en">
<head>
<meta charset="utf-8">
<title>feldreserva – Online Booking System for all sports</title>
<link rel="stylesheet" href="https://fonts.googleapis.com/css2?family=Play:wght@400;700&family=Poppins:wght@400;500;600;700&display=swap">
<style>
  :root {
    --navy: #0c1391;
    --navy-deep: #0a0f7e;
    --band: #0b1699;
    --heading: #111c96;
    --yellow: #ffc800;
    --white: #ffffff;
    --ink: #1b1b1b;
    --muted: #a3a3a3;
    --field: #d9d9d9;
    --tick: #4fd16c;
    --cross: #ff4d4d;
    --footer: #080b55;
  }
  * { box-sizing: border-box; margin: 0; padding: 0; }
  html, body { width: 1200px; height: 3654px; overflow: hidden; }
  body {
    position: relative;
    font-family: "Poppins", sans-serif;
    color: var(--ink);
    background: var(--white);
  }
  .abs { position: absolute; }
  .layer-shapes { position: absolute; left: 0; top: 0; z-index: 1; }
  .content { position: absolute; z-index: 2; }

  .heading {
    font-family: "Play", sans-serif;
    font-weight: 700;
    font-size: 31px;
    text-align: center;
    width: 1200px;
    left: 0;
  }

  .btn {
    display: flex; align-items: center; justify-content: center; gap: 8px;
    background: var(--yellow);
    color: var(--ink);
    font-family: "Poppins", sans-serif;
    font-weight: 600;
    font-size: 13px;
    border-radius: 2px;
    white-space: nowrap;
  }
  .btn svg { width: 12px; height: 8px; }

  /* Header */
  .site-header { left: 0; top: 0; width: 1200px; height: 85px; background: var(--navy); z-index: 3; }
  .brand { left: 128px; top: 22px; display: flex; align-items: center; gap: 10px; }
  .brand-mark { width: 40px; height: 40px; background: var(--yellow); border-radius: 4px; }
  .brand-name { font-family: "Play", sans-serif; font-weight: 700; font-size: 27px; color: var(--yellow); letter-spacing: .3px; }
  .nav { left: 0; top: 0; width: 1200px; height: 85px; }
  .nav a { position: absolute; top: 29px; color: var(--white); text-decoration: none; font-size: 12px; height: 26px; line-height: 26px; white-space: nowrap; }
  .nav a.is-active { color: var(--yellow); border: 1px solid var(--yellow); border-radius: 2px; padding: 0 13px; line-height: 24px; }
  .btn-header { left: 893px; top: 26px; width: 179px; height: 32px; font-size: 12px; }

  /* Hero */
  .hero-photo { left: 0; top: 85px; width: 1200px; height: 540px;
    background: linear-gradient(100deg, #15131a 0%, #2a2724 35%, #3b3630 55%, #1e1c22 80%, #121016 100%); }
  .hero-title { left: 153px; top: 228px; font-family: "Poppins", sans-serif; font-weight: 700; font-size: 33px; line-height: 43px; color: var(--white); }
  .btn-hero { left: 155px; top: 348px; width: 122px; height: 31px; }
  .hero-device { left: 560px; top: 228px; width: 430px; height: 280px; border-radius: 16px;
    background: linear-gradient(160deg, #4a4c55 0%, #d9dbe6 12%, #f3f3f8 50%, #c9cbd6 88%, #55575f 100%); z-index: 2; }

  /* Features */
  .features-title { top: 616px; color: var(--heading); }
  .feature { width: 300px; text-align: center; }
  .feature-icon { width: 86px; height: 86px; margin: 0 auto; border-radius: 50%; background: var(--navy); border: 5px solid var(--yellow); display: flex; align-items: center; justify-content: center; }
  .feature-icon svg { width: 40px; height: 40px; }
  .feature-label { margin-top: 10px; font-size: 14.5px; font-weight: 500; color: var(--ink); }
  .feature-text { margin: 4px auto 0; width: 190px; font-size: 11px; line-height: 16px; color: var(--muted); }
  .btn-features { left: 516px; top: 1052px; width: 168px; height: 32px; }

  /* About */
  .about-photo-frame { left: 176px; top: 1318px; width: 300px; height: 266px; background: var(--yellow); border-radius: 10px; }
  .about-photo { left: 184px; top: 1243px; width: 371px; height: 334px; border-radius: 10px;
    background: linear-gradient(120deg, #6f7b58 0%, #a7a58a 30%, #e0533d 45%, #8f9296 70%, #b8bcc0 100%); }
  .about-copy { left: 613px; top: 1248px; width: 420px; color: var(--white); }
  .about-title { font-family: "Play", sans-serif; font-weight: 700; font-size: 31px; color: var(--yellow); }
  .about-lead { margin-top: 24px; font-weight: 700; font-size: 14.5px; line-height: 21px; }
  .about-text { margin-top: 20px; font-size: 11.5px; line-height: 20px; }
  .btn-about { left: 613px; top: 1533px; width: 136px; height: 31px; }

  /* News */
  .news-title { top: 1724px; color: var(--heading); }
  .news-photo { width: 300px; height: 187px; }
  .news-card { width: 279px; background: var(--white); box-shadow: 0 4px 18px rgba(0,0,0,.12); padding: 20px 18px 16px 17px; display: flex; gap: 18px; }
  .news-date { width: 48px; flex: none; }
  .news-day { font-family: "Play", sans-serif; font-weight: 700; font-size: 27px; line-height: 28px; color: var(--yellow); }
  .news-month { font-size: 10px; color: #666; }
  .news-headline { font-size: 14px; line-height: 19px; color: var(--ink); }
  .news-more { display: inline-block; margin-top: 10px; font-size: 11.5px; color: var(--yellow); text-decoration: underline; }
  .btn-news { left: 545px; top: 2113px; width: 110px; height: 33px; background: #000; color: var(--yellow); }

  /* Pricing */
  .pricing-title { top: 2284px; color: var(--yellow); }
  .price-table { left: 128px; top: 2359px; width: 919px; table-layout: fixed; border-collapse: collapse; color: var(--white); font-size: 11.5px; }
  .price-table th, .price-table td { height: 28.3px; text-align: center; padding: 0; }
  .price-table th { height: 77px; font-weight: 400; font-size: 16px; line-height: 22px; vertical-align: middle; }
  .price-table .plan-price { color: var(--yellow); font-weight: 600; }
  .price-table .plan-price small { color: var(--white); font-weight: 400; font-size: 14px; }
  .price-table .row-label { text-align: left; padding-left: 13px; }
  .price-table col.c-label { width: 183px; }
  .price-table col.c-plan { width: 184px; }
  .price-table col.c-free, .price-table col.c-standard { background: rgba(40,60,220,.45); }
  .price-table col.c-basic, .price-table col.c-premium { background: rgba(5,10,110,.35); }
  .price-table tbody tr:nth-child(odd) td.row-label { background: rgba(60,80,235,.55); }
  .price-table tbody tr:nth-child(even) td.row-label { background: rgba(5,10,110,.25); }
  .price-table svg { width: 11px; height: 11px; vertical-align: middle; }
  .btn-trial { left: 511px; top: 2824px; width: 180px; height: 31px; }

  /* Inquiry */
  .inquiry-title { top: 3006px; color: var(--yellow); }
  .field { border: 1px solid var(--field); background: var(--white); display: flex; align-items: center; gap: 8px; padding: 0 10px; font-size: 10.5px; color: var(--muted); }
  .field svg { width: 12px; height: 12px; flex: none; }
  .field-message { align-items: flex-start; padding-top: 9px; }
  .btn-submit { left: 549px; top: 3224px; width: 102px; height: 31px; }

  /* Footer */
  .footer-photo { left: 0; top: 3230px; width: 1200px; height: 400px;
    background: linear-gradient(180deg, #0a0e6a 0%, var(--footer) 60%, #060842 100%); }
  .footer-brand { left: 126px; top: 3400px; width: 300px; color: var(--white); }
  .footer-mark { width: 40px; height: 40px; background: var(--yellow); border-radius: 4px; margin-left: 65px; }
  .footer-name { margin-top: 8px; font-family: "Play", sans-serif; font-weight: 700; font-size: 27px; color: var(--yellow); }
  .footer-about { margin-top: 18px; font-size: 12px; line-height: 20px; width: 300px; }
  .footer-heading { font-family: "Play", sans-serif; font-weight: 700; font-size: 17px; color: var(--yellow); display: flex; align-items: center; gap: 6px; }
  .footer-heading::after { content: ""; width: 16px; height: 1px; background: var(--yellow); }
  .footer-links { left: 530px; top: 3398px; }
  .footer-links ul { list-style: none; margin-top: 12px; }
  .footer-links li { font-size: 13px; line-height: 22.6px; color: var(--white); }
  .footer-links li.is-active { color: var(--yellow); text-decoration: underline; }
  .footer-contact { left: 750px; top: 3398px; color: var(--white); font-size: 12.5px; }
  .contact-row { display: flex; gap: 12px; align-items: flex-start; margin-top: 16px; line-height: 18px; }
  .contact-row svg { width: 17px; height: 17px; flex: none; }
  .social { left: 1024px; width: 28px; height: 28px; border-radius: 50%; display: flex; align-items: center; justify-content: center; }
  .social span { width: 7px; height: 7px; border-radius: 50%; background: var(--white); }
  .social.is-active { background: var(--yellow); }
  .social.is-active span { background: var(--navy); }
  .copyright { left: 0; top: 3620px; width: 1200px; height: 34px; background: var(--yellow); font-size: 10.5px; text-align: center; line-height: 34px; color: #333; }
</style>
</head>
<body>

<svg width="0" height="0" style="position:absolute">
  <defs>
    <symbol id="i-arrow" viewBox="0 0 12 8"><path d="M0 4h10M7 1l3 3-3 3" fill="none" stroke="currentColor" stroke-width="1.6"/></symbol>
    <symbol id="i-tick" viewBox="0 0 12 12"><path d="M1.5 6.5l3 3 6-7" fill="none" stroke="#4fd16c" stroke-width="2.2" stroke-linecap="round"/></symbol>
    <symbol id="i-cross" viewBox="0 0 12 12"><path d="M2 2l8 8M10 2l-8 8" fill="none" stroke="#ff4d4d" stroke-width="2.2" stroke-linecap="round"/></symbol>
  </defs>
</svg>

<div class="abs hero-photo" role="img" aria-label="Photo of two tennis players giving a high five, dark toned"></div>
<div class="abs footer-photo" role="img" aria-label="Dark blue toned photo of tennis players"></div>

<svg class="layer-shapes" width="1200" height="3654" viewBox="0 0 1200 3654" aria-hidden="true">
  <ellipse cx="747" cy="522" rx="172" ry="40" fill="none" stroke="#ffc800" stroke-width="9"/>
  <path d="M0 608 Q700 420 1200 455 L1200 560 Q700 460 0 612 Z" fill="#ffc800"/>
  <path d="M0 610 Q700 450 1200 555 L1200 640 L0 640 Z" fill="#ffffff"/>

  <path d="M0 1218 Q600 1080 1200 1188 L1200 1598 Q600 1726 0 1598 Z" fill="#ffc800"/>
  <path d="M0 1228 Q600 1095 1200 1198 L1200 1590 Q600 1698 0 1592 Z" fill="#0b1699"/>

  <path d="M0 2292 Q600 2145 1200 2278 L1200 2886 Q600 3006 0 2878 Z" fill="#ffc800"/>
  <path d="M0 2300 Q600 2163 1200 2286 L1200 2880 Q600 2982 0 2872 Z" fill="#0b1699"/>

  <path d="M0 3225 L0 3252 Q600 3456 1200 3252 L1200 3225 Z" fill="#ffc800"/>
  <path d="M0 3225 L0 3246 Q600 3432 1200 3246 L1200 3225 Z" fill="#ffffff"/>
</svg>

<header class="abs site-header">
  <div class="abs brand">
    <div class="brand-mark"></div>
    <div class="brand-name">feldreserva</div>
  </div>
  <nav class="abs nav">
    <a class="is-active" href="#" style="left:434px">Home</a>
    <a href="#" style="left:511px">Features</a>
    <a href="#" style="left:590px">About Us</a>
    <a href="#" style="left:673px">News</a>
    <a href="#" style="left:733px">Pricing</a>
    <a href="#" style="left:801px">Contact Us</a>
  </nav>
  <a class="abs btn btn-header">Reservations / Booking</a>
</header>

<section class="content" style="left:0;top:0;width:1200px;height:640px">
  <h1 class="abs hero-title">Online Booking<br>System for all sports</h1>
  <a class="abs btn btn-hero">Book Now <svg><use href="#i-arrow"/></svg></a>
  <div class="abs hero-device" role="img" aria-label="Tablet with keyboard showing the booking dashboard"></div>
</section>

<section class="content" style="left:0;top:0;width:1200px">
  <h2 class="abs heading features-title">Features</h2>

  <div class="abs feature" style="left:128px;top:704px">
    <div class="feature-icon"><svg viewBox="0 0 40 40" fill="none" stroke="#fff" stroke-width="1.8"><rect x="8" y="8" width="24" height="17" rx="1"/><path d="M5 29h30M14 13h5M14 17h5M22 13h5M22 17h5"/></svg></div>
    <div class="feature-label">Accept online bookings</div>
    <div class="feature-text">Lorem Ipsum is simply dummy text of the printing and...</div>
  </div>
  <div class="abs feature" style="left:450px;top:704px">
    <div class="feature-icon"><svg viewBox="0 0 40 40" fill="none" stroke="#fff" stroke-width="1.8"><rect x="12" y="5" width="16" height="30" rx="2.5"/><path d="M17 30h6M16 13h8M16 17h6"/></svg></div>
    <div class="feature-label">Notifications via SMS/Email</div>
  </div>
  <div class="abs feature" style="left:772px;top:704px">
    <div class="feature-icon"><svg viewBox="0 0 40 40" fill="none" stroke="#fff" stroke-width="1.8"><rect x="6" y="10" width="28" height="19" rx="2"/><path d="M6 16h28M22 24h8"/><circle cx="12" cy="28" r="5" stroke="#ffc800"/><path d="M10 28l1.5 1.5L14 26.5" stroke="#ffc800"/></svg></div>
    <div class="feature-label">Accept Payments</div>
  </div>

  <div class="abs feature" style="left:128px;top:886px">
    <div class="feature-icon"><svg viewBox="0 0 40 40" fill="none" stroke="#fff" stroke-width="1.8"><path d="M4 31l8-12h16l8 12Z"/><path d="M20 22s-5-5-5-9a5 5 0 0110 0c0 4-5 9-5 9Z"/><circle cx="20" cy="13" r="1.8" fill="#fff"/></svg></div>
    <div class="feature-label">Multiple location</div>
  </div>
  <div class="abs feature" style="left:450px;top:886px">
    <div class="feature-icon"><svg viewBox="0 0 40 40" fill="none" stroke="#fff" stroke-width="1.8"><rect x="6" y="8" width="28" height="19" rx="1.5"/><rect x="22" y="17" width="9" height="14" rx="1.5" fill="#0c1391"/><rect x="8" y="22" width="7" height="10" rx="1" fill="#0c1391"/><path d="M16 31h5"/></svg></div>
    <div class="feature-label">Book anywhere</div>
  </div>
  <div class="abs feature" style="left:772px;top:886px">
    <div class="feature-icon"><svg viewBox="0 0 40 40" fill="none" stroke="#fff" stroke-width="1.8"><circle cx="15" cy="14" r="5"/><circle cx="26" cy="15" r="4"/><path d="M6 30c0-5 4-8 9-8s8 2 9 5M26 22c3 0 6 2 7 4"/><path d="M26 30l3 3 6-6" stroke="#ffc800"/></svg></div>
    <div class="feature-label">Group Bookings</div>
  </div>

  <a class="abs btn btn-features">View All Features <svg><use href="#i-arrow"/></svg></a>
</section>

<section class="content" style="left:0;top:0;width:1200px">
  <div class="abs about-photo-frame"></div>
  <div class="abs about-photo" role="img" aria-label="Photo of a young woman and man in sportswear smiling at each other"></div>
  <div class="abs about-copy">
    <h2 class="about-title">About Us</h2>
    <p class="about-lead">Lorem Ipsum is simply dummy text of the printing and typesetting industry.</p>
    <p class="about-text">Lorem Ipsum has been the industry's standard dummy text ever since the 1500s, when an unknown printer took a galley of type and scrambled it to make a type specimen book.</p>
    <p class="about-text">It has survived not only five centuries, but also the leap into electronic typesetting, remaining essentially unchanged...</p>
  </div>
  <a class="abs btn btn-about">Explore More <svg><use href="#i-arrow"/></svg></a>
</section>

<section class="content" style="left:0;top:0;width:1200px">
  <h2 class="abs heading news-title">News</h2>

  <div class="abs news-photo" style="left:128px;top:1806px;background:linear-gradient(135deg,#a34a2e 0%,#c8383f 40%,#d7e04a 60%,#5a8a3a 100%)" role="img" aria-label="Photo of a tennis ball in front of a net"></div>
  <article class="abs news-card" style="left:138px;top:1952px;height:112px">
    <div class="news-date"><div class="news-day">15</div><div class="news-month">Apr, 21</div></div>
    <div><div class="news-headline">Lorem Ipsum is simply dummy text of the printing industry.</div><a class="news-more">Explore More</a></div>
  </article>

  <div class="abs news-photo" style="left:450px;top:1806px;background:linear-gradient(135deg,#3a3a3a 0%,#8c8c8c 45%,#d8d8d8 80%,#f0f0f0 100%)" role="img" aria-label="Photo of a man cheering at his laptop"></div>
  <article class="abs news-card" style="left:460px;top:1929px;height:114px">
    <div class="news-date"><div class="news-day">20</div><div class="news-month">Apr, 21</div></div>
    <div><div class="news-headline">Lorem Ipsum is simply dummy text of the printing industry.</div><a class="news-more">Explore More</a></div>
  </article>

  <div class="abs news-photo" style="left:772px;top:1806px;background:linear-gradient(135deg,#3b2a1c 0%,#8a6a48 40%,#c9ae84 65%,#f1e6d2 100%)" role="img" aria-label="Photo of a laptop and coffee cup on a desk"></div>
  <article class="abs news-card" style="left:782px;top:1952px;height:112px">
    <div class="news-date"><div class="news-day">23</div><div class="news-month">Apr, 21</div></div>
    <div><div class="news-headline">Lorem Ipsum is simply dummy text of the printing industry.</div><a class="news-more">Explore More</a></div>
  </article>

  <a class="abs btn btn-news">View All <svg><use href="#i-arrow"/></svg></a>
</section>

<section class="content" style="left:0;top:0;width:1200px">
  <h2 class="abs heading pricing-title">Pricing</h2>
  <table class="abs price-table">
    <colgroup>
      <col class="c-label"><col class="c-plan c-free"><col class="c-plan c-basic"><col class="c-plan c-standard"><col class="c-plan c-premium">
    </colgroup>
    <thead>
      <tr>
        <th></th>
        <th>Free</th>
        <th>Basic<br><span class="plan-price">$9.9<small>/month*</small></span></th>
        <th>Standard<br><span class="plan-price">$29.9<small>/month*</small></span></th>
        <th>Premium<br><span class="plan-price">$59.9<small>/month*</small></span></th>
      </tr>
    </thead>
    <tbody>
      <tr><td class="row-label">Included bookings</td><td>50</td><td>100</td><td>500</td><td>2000</td></tr>
      <tr><td class="row-label">Custom Features</td><td>1</td><td>3</td><td>8</td><td>unlimited</td></tr>
      <tr><td class="row-label">Users/Providers</td><td>10</td><td>15</td><td>25</td><td>50</td></tr>
      <tr><td class="row-label">Admin App</td><td><svg><use href="#i-tick"/></svg></td><td><svg><use href="#i-tick"/></svg></td><td><svg><use href="#i-tick"/></svg></td><td><svg><use href="#i-tick"/></svg></td></tr>
      <tr><td class="row-label">Client App</td><td><svg><use href="#i-cross"/></svg></td><td><svg><use href="#i-tick"/></svg></td><td><svg><use href="#i-tick"/></svg></td><td>Branded</td></tr>
      <tr><td class="row-label">Booking Website</td><td><svg><use href="#i-tick"/></svg></td><td><svg><use href="#i-tick"/></svg></td><td><svg><use href="#i-tick"/></svg></td><td><svg><use href="#i-tick"/></svg></td></tr>
      <tr><td class="row-label">Booking Widget</td><td><svg><use href="#i-tick"/></svg></td><td><svg><use href="#i-tick"/></svg></td><td><svg><use href="#i-tick"/></svg></td><td><svg><use href="#i-tick"/></svg></td></tr>
      <tr><td class="row-label">Directory Listing</td><td><svg><use href="#i-tick"/></svg></td><td><svg><use href="#i-tick"/></svg></td><td><svg><use href="#i-tick"/></svg></td><td><svg><use href="#i-tick"/></svg></td></tr>
      <tr><td class="row-label">Coupons &amp; Gift Cards</td><td><svg><use href="#i-cross"/></svg></td><td><svg><use href="#i-tick"/></svg></td><td><svg><use href="#i-tick"/></svg></td><td><svg><use href="#i-tick"/></svg></td></tr>
      <tr><td class="row-label">Sales (POS)</td><td><svg><use href="#i-cross"/></svg></td><td><svg><use href="#i-tick"/></svg></td><td><svg><use href="#i-tick"/></svg></td><td><svg><use href="#i-tick"/></svg></td></tr>
      <tr><td class="row-label">Link Removal</td><td><svg><use href="#i-cross"/></svg></td><td><svg><use href="#i-cross"/></svg></td><td><svg><use href="#i-cross"/></svg></td><td><svg><use href="#i-tick"/></svg></td></tr>
      <tr><td class="row-label">HIPAA</td><td><svg><use href="#i-cross"/></svg></td><td><svg><use href="#i-cross"/></svg></td><td><svg><use href="#i-tick"/></svg></td><td><svg><use href="#i-tick"/></svg></td></tr>
    </tbody>
  </table>
  <a class="abs btn btn-trial">Start free Trial Now! <svg><use href="#i-arrow"/></svg></a>
</section>

<section class="content" style="left:0;top:0;width:1200px">
  <h2 class="abs heading inquiry-title">Quick Inquiry</h2>
  <div class="abs field" style="left:302px;top:3074px;width:291px;height:33px">
    <svg viewBox="0 0 12 12" fill="none" stroke="#ffc800" stroke-width="1.2"><circle cx="6" cy="4" r="2.5"/><path d="M1.5 11.5c0-2.5 2-4 4.5-4s4.5 1.5 4.5 4"/></svg>Name
  </div>
  <div class="abs field" style="left:302px;top:3118px;width:291px;height:34px">
    <svg viewBox="0 0 12 12" fill="none" stroke="#ffc800" stroke-width="1.2"><rect x="1" y="2.5" width="10" height="7"/><path d="M1 2.5l5 4 5-4"/></svg>Email
  </div>
  <div class="abs field" style="left:302px;top:3163px;width:291px;height:33px">
    <svg viewBox="0 0 12 12" fill="none" stroke="#ffc800" stroke-width="1.2"><rect x="3" y="1" width="6" height="10" rx="1"/></svg>Phone
  </div>
  <div class="abs field field-message" style="left:607px;top:3074px;width:291px;height:122px">
    <svg viewBox="0 0 12 12" fill="none" stroke="#ffc800" stroke-width="1.2"><path d="M1 1.5h10v7H5l-3 2v-2H1Z"/></svg>Message
  </div>
  <a class="abs btn btn-submit">Submit <svg><use href="#i-arrow"/></svg></a>
</section>

<footer class="content" style="left:0;top:0;width:1200px">
  <div class="abs footer-brand">
    <div class="footer-mark"></div>
    <div class="footer-name">feldreserva</div>
    <p class="footer-about">Lorem Ipsum is simply dummy text of the printing and typesetting industry. Lorem Ipsum has been the industry's...</p>
  </div>

  <div class="abs footer-links">
    <h3 class="footer-heading">Quick Links</h3>
    <ul>
      <li class="is-active">Home</li>
      <li>Features</li>
      <li>About Us</li>
      <li>News</li>
      <li>Pricing</li>
      <li>Contact Us</li>
    </ul>
  </div>

  <div class="abs footer-contact">
    <h3 class="footer-heading">Contact Info</h3>
    <div class="contact-row">
      <svg viewBox="0 0 17 17" fill="none" stroke="#ffc800" stroke-width="1.3"><path d="M4 1.5l3 3-2 2c1 2 3 4 5 5l2-2 3 3-2 2C7 14 3 10 2 3.5Z"/></svg>(555) 214-0937
    </div>
    <div class="contact-row">
      <svg viewBox="0 0 17 17" fill="none" stroke="#ffc800" stroke-width="1.3"><rect x="1.5" y="3.5" width="14" height="10"/><path d="M1.5 3.5l7 6 7-6"/></svg>info@feldreserva.net
    </div>
    <div class="contact-row">
      <svg viewBox="0 0 17 17" fill="none" stroke="#ffc800" stroke-width="1.3"><path d="M8.5 16s-5-5.5-5-9.5a5 5 0 0110 0c0 4-5 9.5-5 9.5Z"/><circle cx="8.5" cy="6.5" r="2"/></svg>
      <span>Level 7, 42 Harbour Lane,<br>Sydney, Australia</span>
    </div>
  </div>

  <div class="abs social" style="top:3406px"><span></span></div>
  <div class="abs social is-active" style="top:3441px"><span></span></div>
  <div class="abs social" style="top:3477px"><span></span></div>
  <div class="abs social" style="top:3512px"><span></span></div>

  <div class="abs copyright">Copyright © 2021 feldreserva. All Rights Reserved</div>
</footer>

</body>
</html>
```